Letterhead Design Project

I need letterhead designed for my law firm. It would also be used for web based stuff as well.

Industry/Entity Type

Law Firm

```html
<!DOCTYPE html>
<html lang="en">
<head>
<meta charset="utf-8">
<title>Hartwell &amp; Moreno Letterhead</title>
<link rel="stylesheet" href="https://fonts.googleapis.com/css2?family=Cormorant+SC:wght@600&family=Montserrat:wght@400&family=Open+Sans:wght@400;700&display=swap">
<style>
  :root {
    --backdrop: #d2d3d5;
    --paper: #ffffff;
    --ink: #3a3a3c;
    --ink-soft: #2b2b2b;
    --accent: #1a93c7;
    --rule: #c9c9cb;
    --divider: #9a9a9a;
  }
  * { margin: 0; padding: 0; box-sizing: border-box; }
  html, body {
    width: 1200px; height: 1000px; overflow: hidden;
    background: var(--backdrop);
  }
  .letterhead {
    position: absolute; left: 294px; top: 104px;
    width: 612px; height: 792px;
    background: var(--paper);
  }
  .masthead {
    position: absolute; top: 40px; left: 0; width: 100%;
    text-align: center;
  }
  .firm-name {
    font-family: "Cormorant SC", "Times New Roman", serif;
    font-weight: 600; font-size: 25px; line-height: 26px;
    color: var(--ink); letter-spacing: 0.2px;
  }
  .firm-tagline {
    font-family: "Montserrat", Arial, sans-serif;
    font-size: 10.5px; line-height: 14px; color: var(--ink-soft);
    margin-top: 3px;
  }
  .footer-rule {
    position: absolute; left: 37px; top: 701px;
    width: 538px; height: 2px; background: var(--rule);
  }
  .footer {
    position: absolute; left: 0; top: 726px; width: 100%; height: 40px;
    font-family: "Open Sans", Arial, sans-serif;
  }
  .footer-mark {
    position: absolute; left: 82px; top: 6px; width: 60px;
    font-family: "Cormorant SC", "Times New Roman", serif;
    font-weight: 600; font-size: 11px; line-height: 12px;
    color: var(--accent); text-align: center;
  }
  .footer-divider {
    position: absolute; left: 148px; top: 0; width: 1px; height: 37px;
    background: var(--divider);
  }
  .contact-block { position: absolute; top: 0; }
  .contact-block.address { left: 177px; }
  .contact-block.phone { left: 292px; }
  .contact-block.web { left: 408px; }
  .contact-label {
    font-weight: 700; font-size: 8.5px; line-height: 12px; color: var(--accent);
  }
  .contact-line {
    font-size: 8.5px; line-height: 11.5px; color: var(--ink-soft);
    white-space: nowrap;
  }
</style>
</head>
<body>
  <main class="letterhead">
    <header class="masthead">
      <div class="firm-name">Hartwell &amp; Moreno</div>
      <div class="firm-tagline">Attorneys of Law</div>
    </header>

    <div class="footer-rule"></div>

    <footer class="footer">
      <div class="footer-mark">Hartwell<br>&amp; Moreno</div>
      <div class="footer-divider"></div>
      <div class="contact-block address">
        <div class="contact-label">Address</div>
        <div class="contact-line">238 Linden Avenue</div>
        <div class="contact-line">Arlington, VA 22201</div>
      </div>
      <div class="contact-block phone">
        <div class="contact-label">Phone</div>
        <div class="contact-line">(555) 301-4827</div>
        <div class="contact-line">Toll Free: 800-555-0142</div>
      </div>
      <div class="contact-block web">
        <div class="contact-label">Contact web</div>
        <div class="contact-line">www.hartwellmoreno.com</div>
        <div class="contact-line">Elena@hartwellmoreno.com</div>
      </div>
    </footer>
  </main>
</body>
</html>
```